Wireless Broadband Newspaper AD

We have recently re-branded our company, new logo and website.

Our primary product offering is Wireless Broadband services to region, the target audience generally cannot get ADSL broadband.

We wanted to pose the question "Can't get ADSL ?" to attract the attention of those who are unable to access conventional mass market broadband offerings.

Ad Size should be:
129mm Wide
178mm High

Please find the text for the AD below.

Can't get ADSL ?
Try Fixed Wireless Broadband

* Speeds up to 10Mbit
* Plans from $29.95 per month
* Up to 60GB Download Allowance
* $99 Professional On-site Installation
* No Contracts

http://pelnetlink.com.au
CALL NOW - 1300 47 91 63

-

Target Market(s)

Frequent Internet users, requiring broadband access in their homes.

Industry/Entity Type

It Company

Requirements
Must have
• Ensure that the general branding feel of the existing website is considered, please us similar colours and theme.
• As well as our logo, which you will find attached in EPS format.
• http://pelnetlink.com.au
Nice to have
• Large caption "Can't get ADSL?"

```html
<!DOCTYPE html>
<html lang="en">
<head>
<meta charset="utf-8">
<title>Pelnet Link – Can't get ADSL?</title>
<link rel="stylesheet" href="https://fonts.googleapis.com/css2?family=Roboto:ital,wght@1,700;1,900&family=Open+Sans:wght@400;600&display=swap">
<style>
  :root {
    --brand-red: #e5321c;
    --charcoal: #333333;
    --offer-blue: #1d80c6;
    --white: #ffffff;
    --logo-grey: #4a4a4a;
    --photo-light: #f1f1f1;
    --photo-warm: #d9c4ad;
  }
  * { margin: 0; padding: 0; box-sizing: border-box; }
  html, body { width: 1200px; height: 938px; overflow: hidden; background: var(--white); }
  .ad {
    position: relative;
    width: 1200px;
    height: 938px;
    background: var(--white);
    overflow: hidden;
  }
  .headline-band {
    position: absolute;
    left: 0; top: 0;
    width: 1200px; height: 122px;
    background: var(--brand-red);
    display: flex; align-items: center; justify-content: center;
  }
  .headline {
    font-family: "Roboto", Arial, sans-serif;
    font-weight: 900;
    font-style: italic;
    font-size: 90px;
    color: var(--white);
    letter-spacing: 1px;
  }
  .subhead-band {
    position: absolute;
    left: 0; top: 138px;
    width: 932px; height: 74px;
    background: var(--charcoal);
    clip-path: polygon(0 0, 100% 0, 94% 100%, 0 100%);
    display: flex; align-items: center;
    padding-left: 80px;
  }
  .subhead {
    font-family: "Roboto", Arial, sans-serif;
    font-weight: 700;
    font-style: italic;
    font-size: 44px;
    color: var(--white);
    letter-spacing: 1px;
  }
  .offer-list {
    position: absolute;
    left: 52px; top: 262px;
    list-style: none;
    font-family: "Open Sans", Arial, sans-serif;
    font-size: 42px;
    line-height: 58px;
    color: var(--offer-blue);
  }
  .offer-list li::before { content: "* "; }
  .lifestyle-photo {
    position: absolute;
    left: 750px; top: 456px;
    width: 400px; height: 316px;
    border-radius: 40%;
    background: radial-gradient(ellipse at 55% 50%, var(--photo-warm) 0%, var(--photo-light) 65%, var(--white) 100%);
  }
  .brand {
    position: absolute;
    left: 44px; top: 818px;
    display: flex; align-items: center; gap: 18px;
  }
  .brand-dot {
    width: 56px; height: 56px;
    border-radius: 50%;
    background: var(--brand-red);
  }
  .brand-name {
    font-family: "Open Sans", Arial, sans-serif;
    font-weight: 600;
    font-size: 54px;
    color: var(--logo-grey);
  }
  .web-band {
    position: absolute;
    left: 490px; top: 810px;
    width: 710px; height: 64px;
    background: var(--brand-red);
    clip-path: polygon(6% 0, 100% 0, 100% 100%, 0 100%);
    display: flex; align-items: center;
    padding-left: 100px;
  }
  .call-band {
    position: absolute;
    left: 530px; top: 874px;
    width: 670px; height: 64px;
    background: #1e1e1e;
    clip-path: polygon(0 0, 100% 0, 100% 100%, 6% 100%);
    display: flex; align-items: center;
    padding-left: 48px;
  }
  .web-address, .call-line {
    font-family: "Open Sans", Arial, sans-serif;
    color: var(--white);
  }
  .web-address { font-size: 38px; }
  .call-line { font-size: 34px; }
</style>
</head>
<body>
<main class="ad">
  <header class="headline-band">
    <h1 class="headline">Can’t get ADSL?</h1>
  </header>
  <div class="subhead-band">
    <h2 class="subhead">Try Fixed Wireless Broadband</h2>
  </div>
  <ul class="offer-list">
    <li>Speeds up to 10Mbit</li>
    <li>Plans from $29.95 per month</li>
    <li>Up to 60GB Download Allowance</li>
    <li>$99 Professional On-site Installation</li>
    <li>No Contracts</li>
  </ul>
  <div class="lifestyle-photo" role="img" aria-label="Photo of a young couple sitting on the floor using laptops"></div>
  <div class="brand">
    <span class="brand-dot"></span>
    <span class="brand-name">pelnet link</span>
  </div>
  <div class="web-band"><span class="web-address">http://pelnetlink.com.au</span></div>
  <div class="call-band"><span class="call-line">CALL NOW - 1300 47 91 63</span></div>
</main>
</body>
</html>
```